Lanternfield Billboard - Financial Services Company (Investments, Tax Planning and Insurance)

Our new office has a billboard directly above the office building. We'd like something eye-catching with a strong Call to Action, with the main part of the billboard being under 7 words if possible. We'd like you to include a way to get ahold of us (either our website lanternfieldllc.example or our phone number 302-418-2967. You may also include in small font something to indicate that we've been serving the area since 1980 (the DE area, the tri-state area, the Copperleaf Basin, etc.)

We offer financial planning, tax planning, and insurance, and we help our clients to focus on their goals and happiness by providing everything they need for lifelong wealth under one roof.

Our logos are attached, we use a triangle logo with green and gray. We use the tagline "experience lifelong wealth" but this does not need to be included.

Potential ideas we have seen from other financial companies-
- the concept that the driver spends more time looking at billboards than planning for their retirement
-something along the lines of "everything you need for your finances is in this building right here" planning, investments, taxes, insurance"
-don't spend your time worrying about retirement, let us help you plan for it
-are you working for your money, or is it working for you?
- retirement takes planning, we're here to help
- ready to retire? talk to us
- need investment advice?
- need help investing?
- crossing your fingers isn't a retirement plan. we can help.
- retiring soon? you need help.

Those are just general ideas, please feel free to be creative.

brand colors:
#00b585
#00b185
#000000
#ffffff
#6d6f75
#6d6f75
#6f7074
#021712
#052e24

```html
<!DOCTYPE html>
<html lang="en">
<head>
<meta charset="utf-8">
<title>Lanternfield Billboard</title>
<link rel="stylesheet" href="https://fonts.googleapis.com/css2?family=Montserrat:wght@500;700;800&family=Tinos:wght@400;700&display=swap">
<style>
  :root {
    --brand-green: #00a46f;
    --deep-green: #0a6b4a;
    --dark-band: #00874f;
    --light-band: #5fcf9f;
    --ink: #111111;
    --gray: #55575c;
    --panel: #f1f1f1;
    --stage: #ffffff;
  }
  * { margin: 0; padding: 0; box-sizing: border-box; }
  html, body { width: 923px; height: 1200px; overflow: hidden; background: var(--stage); }
  .canvas { position: relative; width: 923px; height: 1200px; }
  .billboard {
    position: absolute; left: 30px; top: 353px; width: 863px; height: 493px;
    background: linear-gradient(135deg, #f6f6f6 0%, var(--panel) 60%, #ececec 100%);
    overflow: hidden;
  }
  .art { position: absolute; inset: 0; width: 863px; height: 493px; }
  .brand-name {
    position: absolute; left: 40px; top: 22px;
    font-family: "Tinos", serif; font-weight: 400; font-size: 50px; line-height: 1;
    color: var(--brand-green); letter-spacing: -0.5px;
  }
  .since {
    position: absolute; left: 40px; top: 108px;
    font-family: "Montserrat", sans-serif; font-weight: 500; font-size: 12px; color: var(--gray);
  }
  .headline {
    position: absolute; left: 40px; top: 128px;
    font-family: "Tinos", serif; font-weight: 700; color: var(--ink); line-height: 1.22;
  }
  .headline .line { display: block; font-size: 34px; }
  .headline .accent { color: var(--deep-green); font-size: 46px; }
  .rule { position: absolute; left: 41px; top: 255px; width: 245px; height: 2px; background: var(--deep-green); }
  .pitch {
    position: absolute; left: 40px; top: 276px; width: 330px;
    font-family: "Montserrat", sans-serif; font-size: 16px; line-height: 24px; color: var(--gray); font-weight: 500;
  }
  .pitch strong { display: block; color: var(--ink); font-weight: 800; font-size: 15.5px; }
  .phone-pill {
    position: absolute; left: 38px; top: 381px; width: 268px; height: 46px;
    border-radius: 23px; background: var(--brand-green);
    display: flex; align-items: center; gap: 10px; padding-left: 16px;
    font-family: "Montserrat", sans-serif; font-weight: 700; font-size: 27px; color: #fff;
  }
  .phone-pill svg { width: 22px; height: 22px; }
  .website {
    position: absolute; left: 48px; top: 443px;
    display: flex; align-items: center; gap: 12px;
    font-family: "Montserrat", sans-serif; font-weight: 700; font-size: 19px; color: var(--gray);
  }
  .website svg { width: 20px; height: 20px; }
</style>
</head>
<body>
<main class="canvas">
  <section class="billboard">
    <svg class="art" viewBox="0 0 863 493" aria-hidden="false">
      <defs>
        <linearGradient id="photo-tones" x1="0" y1="0" x2="1" y2="1">
          <stop offset="0" stop-color="#e4d8c4"/>
          <stop offset="0.45" stop-color="#a9adb3"/>
          <stop offset="0.75" stop-color="#e8c24a"/>
          <stop offset="1" stop-color="#d9cfc4"/>
        </linearGradient>
      </defs>
      <polygon role="img" aria-label="Photo of a smiling retired couple reviewing finances at a laptop with a piggy bank"
        points="520,0 863,0 863,493 660,493 393,224" fill="url(#photo-tones)"/>
      <polyline class="band-light" points="478,0 352,224 620,493" fill="none" stroke="var(--light-band)" stroke-width="14"/>
      <polyline class="band-dark" points="506,0 380,224 648,493" fill="none" stroke="var(--dark-band)" stroke-width="22"/>
      <polyline class="corner-light" points="520,368 490,394 585,493" fill="none" stroke="var(--light-band)" stroke-width="12"/>
      <polyline class="corner-dark" points="506,352 470,388 568,493" fill="none" stroke="var(--dark-band)" stroke-width="8"/>
    </svg>

    <div class="brand-name">Lanternfield</div>
    <div class="since">since 1980</div>
    <h1 class="headline">
      <span class="line"><span class="accent">Retiring</span> soon?</span>
      <span class="line">You need <span class="accent">help</span></span>
    </h1>
    <div class="rule"></div>
    <p class="pitch">Everything you need for your finances is in this building right here
      <strong>Planning, Investments,</strong>
      <strong>Taxes, Insurance</strong>
    </p>
    <div class="phone-pill">
      <svg viewBox="0 0 24 24" aria-hidden="true"><path fill="#fff" d="M6.6 10.8a15.1 15.1 0 0 0 6.6 6.6l2.2-2.2c.3-.3.7-.4 1-.2 1.1.4 2.3.6 3.6.6.6 0 1 .4 1 1V20c0 .6-.4 1-1 1A17 17 0 0 1 3 4c0-.6.4-1 1-1h3.5c.6 0 1 .4 1 1 0 1.3.2 2.5.6 3.6.1.3 0 .7-.2 1z"/></svg>
      <span>302-418-2967</span>
    </div>
    <div class="website">
      <svg viewBox="0 0 24 24" aria-hidden="true" fill="none" stroke="var(--brand-green)" stroke-width="1.8"><circle cx="12" cy="12" r="10"/><ellipse cx="12" cy="12" rx="4.5" ry="10"/><path d="M2 12h20M4 6.5h16M4 17.5h16"/></svg>
      <span>lanternfieldllc.example</span>
    </div>
  </section>
</main>
</body>
</html>
```